KPFT website

The design should be based on the style and layout of the Tevix website (https://www.tevixorb.ae/about-us) , incorporating softer tones.
Use KPFT green for headers and ash grey for other elements to maintain brand consistency.
The top of the homepage should include a dynamic counter that displays the number of projects we are currently working on and their total value.

Then going into Who we are, Vision, Mission, Directors, Our Values then Current Projects.
The current project wont link to any where right now but would like this option later on.

The bottom of the homepage should feature a section dedicated to showcasing the logos or names of our key clients.

This website will be an essential tool for communicating our expertise and engaging with potential clients, so it should be visually appealing, user-friendly, and aligned with our brand identity.

```html
<!DOCTYPE html>
<html lang="en">
<head>
<meta charset="utf-8">
<title>KPFT</title>
<link href="https://fonts.googleapis.com/css2?family=Krona+One&family=Roboto:wght@400;500;700&display=swap" rel="stylesheet">
<style>
:root{
  --green:#108a68;
  --green-dark:#0c6f5f;
  --teal:#127a6f;
  --ink:#222428;
  --ash:#6b6e72;
  --ash-light:#f2f2f2;
  --footer:#3c3e41;
  --white:#ffffff;
}
*{margin:0;padding:0;box-sizing:border-box}
html,body{width:1200px;height:4342px;overflow:hidden;background:var(--white)}
body{font-family:'Roboto',Arial,sans-serif;color:var(--ink);position:relative}
.abs{position:absolute}
.display{font-family:'Krona One',Arial,sans-serif}
.accent{color:var(--green)}
.btn{position:absolute;display:flex;align-items:center;justify-content:center;background:var(--green);color:var(--white);border-radius:24px;font-weight:500;font-size:15px;height:45px;text-decoration:none}
.photo{position:absolute;display:block}
/* header */
.site-header{position:absolute;left:0;top:0;width:1200px;height:57px;background:var(--white)}
.logo{position:absolute;left:111px;top:10px;font-family:'Krona One',sans-serif;font-size:32px;color:var(--green);letter-spacing:1px}
.main-nav{position:absolute;left:381px;top:0;width:819px;height:57px;background:var(--green);display:flex;align-items:center;justify-content:space-around;padding:0 20px}
.main-nav a{color:var(--white);font-size:12px;font-weight:700;text-decoration:none}
.main-nav a.active{text-decoration:underline}
/* hero */
.hero{position:absolute;left:0;top:57px;width:1200px;height:558px;background:linear-gradient(90deg,#efefee 0%,#ebebea 40%,#d7cfc6 70%,#b9a89a 100%)}
.hero-kicker{left:115px;top:148px;font-size:21px}
.hero-title{left:110px;top:190px;font-size:72px;color:var(--green)}
.hero-text{left:112px;top:282px;width:380px;font-size:15px;line-height:28px}
.dots{position:absolute;left:578px;top:486px;display:flex;gap:6px}
.dots span{width:11px;height:11px;border-radius:50%;background:var(--white)}
.dots span.on{background:var(--green)}
/* sections */
.section-title{position:absolute;font-family:'Krona One',sans-serif;font-size:34px;line-height:42px;color:var(--ink);white-space:nowrap}
.rule{position:absolute;height:3px;background:var(--green)}
.copy{position:absolute;font-size:13px;line-height:28.3px;color:var(--ash)}
/* stats */
.stats{position:absolute;left:0;top:1262px;width:1200px;height:233px;background:linear-gradient(135deg,#0f7a6d 0%,#14857a 50%,#0f7468 100%)}
.stat{position:absolute;top:72px;width:320px;text-align:center;color:var(--white)}
.stat-num{font-family:'Krona One',sans-serif;font-size:40px}
.stat-label{font-size:24px;font-weight:500;margin-top:6px}
.divider{position:absolute;top:78px;width:3px;height:92px;background:var(--white)}
/* cards */
.card-title{position:absolute;top:1874px;font-size:24px;font-weight:500}
.card-text{position:absolute;top:1915px;width:320px;font-size:11.5px;line-height:25.3px;color:var(--ash)}
/* clients */
.clients{position:absolute;left:99px;top:3825px;width:1001px;height:152px;background:var(--ash-light)}
.client{position:absolute;top:56px;font-size:28px;font-weight:500;color:#4a4c50;white-space:nowrap}
/* footer */
.site-footer{position:absolute;left:0;top:3998px;width:1200px;height:344px;background:var(--footer);color:var(--white)}
.footer-logo{position:absolute;left:0;width:1200px;top:82px;text-align:center;font-family:'Krona One',sans-serif;font-size:52px;color:var(--green)}
.footer-nav{position:absolute;top:170px;left:0;width:1200px;display:flex;justify-content:center;gap:19px;font-size:13px;font-weight:500}
.contact{position:absolute;top:222px;display:flex;align-items:center;gap:12px;font-size:15px;white-space:nowrap}
.footer-rule{position:absolute;left:111px;top:290px;width:976px;height:1px;background:#9a9c9f}
.copyright{position:absolute;left:118px;top:310px;font-size:13px}
.social{position:absolute;left:1064px;top:309px;width:18px;height:18px;background:var(--white);border-radius:2px}
</style>
</head>
<body>

<header class="site-header">
  <div class="logo">KPFT</div>
  <nav class="main-nav">
    <a class="active" href="#">Home</a><a href="#">Who we are</a><a href="#">Our Vision</a><a href="#">Our Mission</a><a href="#">Directors</a><a href="#">Our Values</a><a href="#">Contact Us</a>
  </nav>
</header>

<section class="hero" role="img" aria-label="Team working around a meeting table seen from above">
  <div class="abs hero-kicker">Welcome To</div>
  <div class="abs hero-title display">KPFT</div>
  <p class="abs hero-text">Lorem ipsum dolor sit amet, consectetur adipiscing elit, sed do eiusmod tempor</p>
  <a class="btn" style="left:115px;top:364px;width:143px">Get Started</a>
  <div class="dots"><span></span><span class="on"></span><span></span></div>
</section>

<section class="who">
  <div class="photo" role="img" aria-label="Hand holding a phone with glowing cost chart" style="left:111px;top:701px;width:448px;height:473px;background:linear-gradient(160deg,#0d2236,#123a55 55%,#0a1a2a)"></div>
  <h2 class="section-title" style="left:642px;top:700px">Who <span class="accent">We Are</span></h2>
  <div class="rule" style="left:646px;top:748px;width:102px"></div>
  <p class="copy" style="left:642px;top:764px;width:450px">Sed ut perspiciatis unde omnis iste natus error sit voluptatem accusantium doloremque laudantium, totam rem aperiam, eaque ipsa quae ab illo inventore veritatis et quasi architecto beatae vitae dicta sunt explicabo. Nemo enim ipsam voluptatem quia voluptas sit aspernatur aut odit aut fugit, sed quia consequuntur magni dolores eos qui ratione voluptatem sequi nesciunt. Neque porro quisquam est, qui dolorem ipsum quia dolor sit amet, consectetur, adipisci velit, sed quia non numquam eius modi tempora incidunt ut labore et dolore magnam aliquam quaerat voluptatem. Ut enim ad minima veniam, quis nostrum exercitationem ullam corporis suscipit laboriosam, nisi ut aliquid ex ea commodi consequatur? Quis autem vel eum iure reprehenderit qui in ea voluptate velit esse quam nihil</p>
  <a class="btn" style="left:640px;top:1130px;width:144px">Read More</a>
</section>

<section class="stats">
  <div class="stat" style="left:103px"><div class="stat-num">347+</div><div class="stat-label">Number of Projects</div></div>
  <div class="divider" style="left:445px"></div>
  <div class="stat" style="left:448px"><div class="stat-num">374+</div><div class="stat-label">Currently Working</div></div>
  <div class="divider" style="left:779px"></div>
  <div class="stat" style="left:768px"><div class="stat-num">347+</div><div class="stat-label">Total Value</div></div>
</section>

<section class="pillars">
  <div class="photo" role="img" aria-label="Colleagues reviewing papers at a desk" style="left:111px;top:1581px;width:317px;height:269px;background:linear-gradient(150deg,#5a4536,#8a6a4e 50%,#3b3029)"></div>
  <div class="photo" role="img" aria-label="Finger touching a rising glowing bar chart" style="left:441px;top:1581px;width:317px;height:269px;background:linear-gradient(160deg,#1a2a3c,#0f2030 60%,#1d4a66)"></div>
  <div class="photo" role="img" aria-label="Hand touching a digital percentage display" style="left:770px;top:1581px;width:317px;height:269px;background:linear-gradient(160deg,#2a3a4c,#1c2a3a 60%,#3c5066)"></div>
  <h3 class="card-title" style="left:111px">Mission</h3>
  <h3 class="card-title" style="left:441px">Vision</h3>
  <h3 class="card-title" style="left:770px">Values</h3>
  <p class="card-text" style="left:111px">Lorem ipsum dolor sit amet, consectetur adipiscing elit, sed do eiusmod tempor incididunt ut labore et dolore magna aliqua. Ut enim ad minim veniam, quis nostrud exercitation ullamco laboris nisi ut aliquip ex consequat.</p>
  <p class="card-text" style="left:441px">Lorem ipsum dolor sit amet, consectetur adipiscing elit, sed do eiusmod tempor incididunt ut labore et dolore magna aliqua. Ut enim ad minim veniam, quis nostrud exercitation ullamco laboris nisi ut aliquip ex consequat.</p>
  <p class="card-text" style="left:770px">Lorem ipsum dolor sit amet, consectetur adipiscing elit, sed do eiusmod tempor incididunt ut labore et dolore magna aliqua. Ut enim ad minim veniam, quis nostrud exercitation ullamco laboris nisi ut aliquip ex consequat.</p>
</section>

<section class="directors">
  <h2 class="section-title" style="left:108px;top:2098px">Our <span class="accent">Directors</span></h2>
  <div class="rule" style="left:110px;top:2146px;width:88px"></div>
  <p class="copy" style="left:110px;top:2160px;width:450px">Sed ut perspiciatis unde omnis iste natus error sit voluptatem accusantium doloremque laudantium, totam rem aperiam, eaque ipsa quae ab illo inventore veritatis et quasi architecto beatae vitae dicta sunt explicabo. Nemo enim ipsam voluptatem quia voluptas sit aspernatur aut odit aut fugit, sed quia consequuntur magni dolores eos qui ratione voluptatem sequi nesciunt. Neque porro quisquam est, qui dolorem ipsum quia dolor sit amet, consectetur, adipisci velit, sed quia non numquam eius modi tempora incidunt ut labore et dolore magnam aliquam quaerat voluptatem. Ut enim ad minima veniam, quis nostrum exercitationem ullam corporis suscipit laboriosam, nisi ut aliquid ex ea commodi consequatur? Quis autem vel eum iure reprehenderit qui in ea voluptate velit esse quam nihil</p>
  <a class="btn" style="left:107px;top:2528px;width:144px">Read More</a>
  <div class="photo" role="img" aria-label="Three directors in suits gathered around a laptop" style="left:639px;top:2098px;width:448px;height:473px;background:linear-gradient(160deg,#6f7a7e,#b9bfc0 45%,#4a5256)"></div>
</section>

<section class="projects">
  <h2 class="section-title" style="left:0;width:1200px;text-align:center;top:2656px">Current <span class="accent">Projects</span></h2>
  <div class="rule" style="left:551px;top:2703px;width:101px"></div>
  <a class="photo" role="img" aria-label="Presenter at a whiteboard during a meeting" style="left:118px;top:2738px;width:472px;height:464px;background:linear-gradient(150deg,#e2e4e4,#c9cccd 55%,#3d3e44)"></a>
  <a class="photo" role="img" aria-label="Two colleagues talking at a conference table" style="left:607px;top:2738px;width:473px;height:464px;background:linear-gradient(150deg,#d8dad8,#9da4a6 50%,#4b5256)"></a>
  <a class="photo" role="img" aria-label="Two women reviewing charts at a laptop" style="left:118px;top:3227px;width:472px;height:463px;background:linear-gradient(150deg,#dfe2e2,#b7a48c 55%,#6a5544)"></a>
  <a class="photo" role="img" aria-label="Business team discussing documents at a table" style="left:607px;top:3227px;width:473px;height:463px;background:linear-gradient(150deg,#4b5a3c,#6e6a5c 50%,#3a3530)"></a>
</section>

<section class="key-clients">
  <h2 class="section-title" style="left:0;width:1200px;text-align:center;top:3774px">Our Key <span class="accent">Clients</span></h2>
  <div class="clients">
    <div class="client" style="left:58px">NORVEL</div>
    <div class="client" style="left:240px">ALTRIVO</div>
    <div class="client" style="left:425px">Quenta</div>
    <div class="client" style="left:600px">MARLEN</div>
    <div class="client" style="left:782px">OSKAR &amp; CO</div>
  </div>
  <div class="rule" style="left:551px;top:3829px;width:101px"></div>
</section>

<footer class="site-footer">
  <div class="footer-logo">KPFT</div>
  <nav class="footer-nav"><span>Home</span><span>Who we are</span><span>Our Vision</span><span>Our Mission</span><span>Directors</span><span>Our Values</span><span>Contact Us</span></nav>
  <div class="contact" style="left:270px">
    <svg width="30" height="30" viewBox="0 0 30 30"><rect width="30" height="30" rx="4" fill="#fff"/><path d="M15 6a6 6 0 0 0-6 6c0 5 6 12 6 12s6-7 6-12a6 6 0 0 0-6-6z" fill="#3c3e41"/><circle cx="15" cy="12" r="2.3" fill="#fff"/></svg>
    <span>Lorem Ipsum ,Usa -518204</span></div>
  <div class="contact" style="left:549px">
    <svg width="30" height="30" viewBox="0 0 30 30"><rect width="30" height="30" rx="4" fill="#fff"/><path d="M10 7l4 4-2 2c1 2.5 3 4.5 5 5l2-2 4 4-2 3c-6 0-13-7-13-13z" fill="#3c3e41"/></svg>
    <span>+1 555 014 27390</span></div>
  <div class="contact" style="left:805px">
    <svg width="30" height="30" viewBox="0 0 30 30"><rect width="30" height="30" rx="4" fill="#fff"/><rect x="7" y="10" width="16" height="11" fill="#3c3e41"/><path d="M7 10l8 6 8-6" stroke="#fff" stroke-width="1.5" fill="none"/></svg>
    <span>info@kpft.in</span></div>
  <div class="footer-rule"></div>
  <div class="copyright">© 2024 &nbsp;KPFT. All rights reserved.</div>
  <div class="social" aria-label="Social profile"></div>
</footer>

</body>
</html>
```